依頼詳細
PCとスマホデザインの両方納品をいただきますが、
まずはデザインイメージが確認しやすいPCページのみの提案をお願いします。
スマホページは当選者に納品時にお願いしたいと思います。
スマホサイズについて、カンバスサイズは横幅375pxで作成し、2倍の横幅750pxのサイズで書き出ししてください。
(Retinaディスプレイに対応するため)
スマホページ作成時は、メニューが展開した際のデザインもお願いします。
レスポンシブウェブデザインを意識したデザインでお願いします。

■サイトマップ
添付の画面遷移図をご確認ください。

■参考サイト
https://www.hirotoku-sarumi.jp/
https://www.tabuse-seiban.co.jp/

■内容について
主に鋼材の卸売業を行う会社の公式サイトになります。
卸売だけでなく、鋼板を仕入れて希望のサイズに切断、プレスなどの加工も行う会社です。
参考サイトはメインビジュアルが動画になっていますが、今回のサイトデザインでは動画を使用する予定は今のところありません。

■素材写真
画像データについては、フリー素材から流用して
イメージ画像に当て込んでください。
足りない場合は、一旦他のサイトの写真をサンプルとして
入れてください。(サンプルなどの表記をお願いします)
また、購入が必要な写真などを利用した場合、
価格とサイト名を教えてください。

また、Pixoral Imageで定期契約をしていますので、
Pixoral Imageの画像は使用できます。
デザイン時はカンプ画像をお入れいただきますようお願いします。

■ロゴについて
添付のロゴデータを使用してください。

■ワイヤーフレーム
https://mock.velqara.net/view/52817caa-1f3b-4d0e-9a72-6e1b8c37d904-b39f/?fullscreen
コンテンツの構成としてワイヤーフレームを作成しましたが
必ずしもワイヤーフレームの通りではなくて大丈夫です。
TOPページに配置するコンテンツを見ていただき、デザインは
デザイナーの皆様におまかせしたいと思います。

----------------------------------------------------------------------------
【制作物に対するお願い】

■フォントについて
・無料で使えるフォントで作成をお願いします。
・OSに紐づくフォントの使用は控えていただければと思います (ヒラギノなど)

ページ数
1ページ
希望イメージ
シンプル 複雑
単色 カラフル
暗い 明るい
日常 高級
遊び心 厳粛
未来的 伝統的
女性的 男性的
希望する色
ベースカラー:白、青、ポイントカラー:赤
納品ファイル
• 高解像度JPG (.jpg)
• イラストレーター形式 (.ai)
• フォトショップ形式 (.psd)
補足説明
上記のいずれか1つ(アウトラインありとなしの2つ)と高解像度JPGを納品お願いします。
adobe XDでの納品も可能です。
CS5にバージョンを落としたロゴデータです。
ロゴのpngデータも追加しました。

```html
<!DOCTYPE html>
<html lang="ja">
<head>
<meta charset="utf-8">
<title>北浜コウザイ株式会社</title>
<link href="https://fonts.googleapis.com/css2?family=Noto+Sans+JP:wght@400;500;700;900&family=Oswald:wght@500;600&display=swap" rel="stylesheet">
<style>
:root{
  --blue:#0d3a96;
  --blue-deep:#0a2f7d;
  --red:#d7131e;
  --ink:#222;
  --grey:#e9e9e9;
  --white:#fff;
}
*{margin:0;padding:0;box-sizing:border-box}
html,body{width:1200px;height:3480px;overflow:hidden}
body{font-family:"Noto Sans JP",sans-serif;color:var(--ink);background:var(--white);position:relative}
.abs{position:absolute}
.brand{font-weight:900;font-size:22px;letter-spacing:.04em;display:flex;align-items:center;gap:10px}
.brand i{width:14px;height:14px;background:var(--red);display:block}

/* header + hero */
.hero{left:0;top:0;width:1200px;height:760px;background:linear-gradient(160deg,#9a9c9f 0%,#5d6065 45%,#2b2d31 100%)}
.site-header{left:0;top:0;width:1200px;height:60px;display:flex;align-items:center;padding-left:40px;background:rgba(255,255,255,.92)}
.site-header .brand{color:var(--blue)}
.gnav{margin-left:auto;display:flex;height:60px;align-items:center}
.gnav a{font-size:14px;color:var(--ink);text-decoration:none;margin-right:34px;font-weight:500}
.gnav .contact{margin:0;background:var(--red);color:var(--white);height:60px;width:190px;display:flex;align-items:center;justify-content:center;gap:10px}
.hero-lead{left:120px;top:150px;font-size:40px;font-weight:900;color:var(--white);letter-spacing:.04em}
.hero-copy1{left:110px;top:215px;font-size:150px;line-height:1;font-weight:900;color:var(--white);letter-spacing:.02em}
.hero-copy2{left:270px;top:420px;font-size:220px;line-height:1;font-weight:900;color:var(--white);letter-spacing:.04em}

/* about */
.about-band{left:0;top:780px;width:1200px;height:620px;background:var(--blue)}
.about-panel{left:120px;top:1000px;width:1000px;height:560px;background:var(--white)}
.photo{display:block}
.about-photo1{left:160px;top:800px;width:380px;height:420px;background:linear-gradient(150deg,#c9d3de,#6f7d8c 60%,#3b4652)}
.about-photo2{left:160px;top:1220px;width:180px;height:190px;background:linear-gradient(140deg,#7b6a5a,#3a3330)}
.sec-title{display:flex;align-items:center;gap:14px}
.sec-title::before{content:"";width:5px;height:56px;background:var(--red)}
.sec-title .en{font-family:"Oswald",sans-serif;font-weight:600;font-size:58px;line-height:1;letter-spacing:.02em}
.sec-title .ja{font-weight:700;font-size:26px}
.about-title{left:660px;top:810px;color:var(--white)}
.about-sub{left:680px;top:880px;color:var(--white);font-size:26px;font-weight:700}
.about-text{left:680px;top:1060px;width:400px;font-size:14px;line-height:2.3}
.btn{height:54px;width:220px;display:flex;align-items:center;justify-content:center;color:var(--white);font-size:15px;font-weight:500;text-decoration:none}
.btn-blue{background:var(--blue)}
.btn-red{background:var(--red)}
.about-btn1{left:360px;top:1460px}
.about-btn2{left:720px;top:1460px}

/* recruit */
.recruit-photo{left:0;top:1620px;width:1200px;height:500px;background:radial-gradient(circle at 62% 40%,#e59a4a 0%,#7a3f1d 18%,#2a1f1c 45%,#121213 100%)}
.recruit-accent{left:1040px;top:2120px;width:160px;height:240px;background:var(--blue)}
.recruit-card{left:120px;top:1900px;width:960px;height:450px;background:var(--white);border:2px solid #cfcfcf}
.recruit-title{left:155px;top:1945px;color:var(--ink)}
.recruit-title .en{color:var(--blue)}
.recruit-title .ja{color:var(--blue)}
.recruit-text{left:160px;top:2040px;width:560px;font-size:14px;line-height:2.3}
.recruit-staff{left:760px;top:1940px;width:290px;height:280px;background:linear-gradient(180deg,#b9c3cf,#2b3f63 70%,#1e2a44)}
.recruit-btn{left:480px;top:2240px}

/* news */
.news-title{left:0;top:2440px;width:1200px;justify-content:center}
.news-title .en{color:var(--blue)}
.news-title .ja{color:var(--blue)}
.news-accent{left:40px;top:2600px;width:460px;height:480px;background:var(--blue)}
.news-box{left:160px;top:2560px;width:920px;height:440px;background:var(--grey)}
.news-list{left:220px;top:2600px;width:750px;list-style:none}
.news-list li{height:70px;background:var(--white);border:1px solid #cfcfcf;margin-bottom:34px;display:flex;align-items:center;padding-left:50px;font-size:14px}
.news-list .cat{width:110px}
.news-list .date{width:130px;color:var(--blue);font-weight:700}

/* footer */
.site-footer{left:0;top:3140px;width:1200px;height:340px;background:var(--blue);color:var(--white)}
.footer-brand{left:120px;top:3190px;color:var(--white)}
.footer-addr{left:120px;top:3250px;font-size:14px;line-height:1.8}
.footer-contact{left:460px;top:3180px;width:580px;height:140px;border:2px solid var(--white);display:flex}
.footer-contact .tel{flex:1;padding:24px 30px;font-size:13px}
.footer-contact .num{font-size:34px;font-weight:900;display:flex;align-items:center;gap:10px;margin:6px 0 2px}
.footer-contact .mail{width:210px;background:var(--white);color:var(--blue);display:flex;flex-direction:column;align-items:center;justify-content:center;gap:12px;font-size:15px;font-weight:700}
.footer-nav{left:0;top:3400px;width:1200px;display:flex;justify-content:center;gap:52px;font-size:13px}
.copyright{left:0;top:3448px;width:1200px;text-align:center;font-size:11px;opacity:.85}
</style>
</head>
<body>

<div class="abs hero photo" role="img" aria-label="積み上げられた角形鋼管のモノクロ写真"></div>
<header class="abs site-header">
  <div class="brand"><i></i>北浜コウザイ株式会社</div>
  <nav class="gnav">
    <a href="#">事業内容</a><a href="#">会社概要</a><a href="#">採用情報</a>
    <a href="#" class="contact">
      <svg width="20" height="14" viewBox="0 0 20 14"><rect x="1" y="1" width="18" height="12" fill="none" stroke="#fff" stroke-width="2"/><path d="M1 1l9 7 9-7" fill="none" stroke="#fff" stroke-width="2"/></svg>お問い合わせ</a>
  </nav>
</header>
<p class="abs hero-lead">北浜コウザイ株式会社は挑戦し続けます</p>
<h1 class="abs hero-copy1">ものづくりの</h1>
<p class="abs hero-copy2">創造へ</p>

<section>
  <div class="abs about-band"></div>
  <div class="abs about-panel"></div>
  <div class="abs about-photo1 photo" role="img" aria-label="鋼材が並ぶ広い倉庫の写真"></div>
  <div class="abs about-photo2 photo" role="img" aria-label="鋼材を加工する作業現場の写真"></div>
  <h2 class="abs sec-title about-title"><span class="en">ABOUT</span></h2>
  <p class="abs about-sub">北浜コウザイについて</p>
  <p class="abs about-text">北浜コウザイは鋼材の卸売を中心に、鋼板の仕入れから切断、プレス加工までを一貫して行っています。お客様のご希望のサイズと品質に合わせ、確かな技術で迅速にお届けします。地域のものづくりを支える存在として、これからも挑戦を続け、信頼される企業であり続けることを目指しています。</p>
  <a href="#" class="abs btn btn-blue about-btn1">事業内容</a>
  <a href="#" class="abs btn btn-blue about-btn2">会社概要</a>
</section>

<section>
  <div class="abs recruit-photo photo" role="img" aria-label="火花を散らす溶接作業の写真"></div>
  <div class="abs recruit-accent"></div>
  <div class="abs recruit-card"></div>
  <h2 class="abs sec-title recruit-title"><span class="en">RECRUIT</span><span class="ja">採用情報</span></h2>
  <p class="abs recruit-text">北浜コウザイでは、ものづくりに情熱を持つ仲間を募集しています。未経験の方でも先輩社員が丁寧に指導しますので安心です。鋼材の知識と加工技術を身につけ、一緒に成長していきませんか。あなたの挑戦を心よりお待ちしています。</p>
  <div class="abs recruit-staff photo" role="img" aria-label="作業着姿の社員の集合写真"></div>
  <a href="#" class="abs btn btn-red recruit-btn">採用情報</a>
</section>

<section>
  <h2 class="abs sec-title news-title"><span class="en">NEWS</span><span class="ja">お知らせ</span></h2>
  <div class="abs news-accent"></div>
  <div class="abs news-box"></div>
  <ul class="abs news-list">
    <li><span class="cat">お知らせ</span><span class="date">20XX.XX.XX</span>ホームページリニューアル</li>
    <li><span class="cat">お知らせ</span><span class="date">20XX.XX.XX</span>ホームページリニューアル</li>
    <li><span class="cat">お知らせ</span><span class="date">20XX.XX.XX</span>ホームページリニューアル</li>
  </ul>
</section>

<footer>
  <div class="abs site-footer"></div>
  <div class="abs brand footer-brand"><i></i>北浜コウザイ株式会社</div>
  <p class="abs footer-addr" style="color:#fff">〒950-0123 北浜市港町1-2-3<br>TEL：0120-55-7310<br>FAX：0120-55-7311</p>
  <div class="abs footer-contact" style="color:#fff">
    <div class="tel">ご相談やご依頼など、お気軽にお問い合わせください。
      <div class="num"><svg width="26" height="26" viewBox="0 0 24 24"><path fill="#fff" d="M6.6 10.8a15 15 0 006.6 6.6l2.2-2.2a1 1 0 011-.25 11.4 11.4 0 003.6.57 1 1 0 011 1V20a1 1 0 01-1 1A17 17 0 013 4a1 1 0 011-1h3.5a1 1 0 011 1c0 1.25.2 2.45.57 3.57a1 1 0 01-.25 1z"/></svg>0120-55-7310</div>
      受付時間 9:00〜17:00（土日祝休み）</div>
    <div class="mail">
      <svg width="50" height="36" viewBox="0 0 50 36"><rect x="2" y="2" width="46" height="32" fill="#0d3a96"/><path d="M2 2l23 18L48 2" fill="none" stroke="#fff" stroke-width="3"/></svg>お問い合わせ</div>
  </div>
  <nav class="abs footer-nav" style="color:#fff"><span>TOPページ</span><span>事業内容</span><span>会社概要</span><span>採用情報</span><span>お問い合わせ</span><span>プライバシーポリシー</span><span>サイトポリシー</span></nav>
  <p class="abs copyright" style="color:#fff">© 北浜コウザイ All Rights Reserved.</p>
</footer>

</body>
</html>
```